Pellmont Industries Line Card

Hello - We're looking to develop a two sided brochure for our company product lines and capabilities. We're a distributor, value-added reseller, we build cable assemblies and panel assemblies. Looking for a flyer to help tell our story. Our primary market is selling to customers in the off-highway equipment markets. Construction, AG and Specialty Vehicles.

```html
<!DOCTYPE html>
<html lang="en">
<head>
<meta charset="utf-8">
<title>Pellmont Industries Line Card</title>
<link href="https://fonts.googleapis.com/css2?family=Oswald:wght@500;600&family=Ubuntu:wght@400;500;700&display=swap" rel="stylesheet">
<style>
:root{
  --red:#e31b23;
  --dark:#434345;
  --darker:#2a2a2b;
  --black:#000;
  --paper:#f0f0f0;
  --white:#fff;
  --ring:#c9c9c9;
}
*{box-sizing:border-box;margin:0;padding:0}
html,body{width:1200px;height:1177px;overflow:hidden;background:var(--black)}
.stage{position:relative;width:1200px;height:1177px;background:var(--black)}
.page{position:absolute;top:206px;width:529px;height:689px;background:var(--paper);overflow:hidden}
.page-front{left:60px}
.page-back{left:616px;width:530px}
.abs{position:absolute}
.header-shapes{position:absolute;left:0;top:0}
.brand{position:absolute;display:flex;align-items:center;gap:7px;font-family:"Oswald",sans-serif;font-weight:600;color:var(--darker);text-transform:uppercase;letter-spacing:.5px;line-height:1}
.brand-mark{width:12px;height:12px;background:var(--red);flex:none}
.url{position:absolute;font-family:"Ubuntu",sans-serif;font-weight:700;color:var(--white)}
.title{position:absolute;font-family:"Oswald",sans-serif;font-weight:500;color:var(--white);text-transform:uppercase;line-height:1.1}
.address{position:absolute;font-family:"Ubuntu",sans-serif;font-weight:500;color:var(--white);font-size:10.5px;display:flex;align-items:center;gap:6px;letter-spacing:.3px}
.octagon{clip-path:polygon(29% 0,71% 0,100% 29%,100% 71%,71% 100%,29% 100%,0 71%,0 29%)}
/* product rows */
.line{position:absolute;left:10px;width:364px;height:62px}
.line-bar{position:absolute;left:60px;top:8px;width:302px;height:44px;background:var(--dark);box-shadow:2px 2px 3px rgba(0,0,0,.25)}
.line-accent{position:absolute;right:0;top:0;width:140px;height:100%;background:var(--red)}
.line-list{position:absolute;top:4px;list-style:none;font-family:"Ubuntu",sans-serif;font-size:9px;line-height:11px;color:var(--white)}
.line-list li::before{content:"• "}
.list-main{left:22px}
.list-accent{left:168px}
.badge{position:absolute;left:0;top:0;width:62px;height:62px;background:var(--ring);padding:3px}
.badge-face{width:100%;height:100%;background:var(--white);display:flex;align-items:center;justify-content:center;text-align:center;font-family:"Ubuntu",sans-serif;font-weight:700;font-size:9px;line-height:1.1;color:#1d4f91}
.badge-red{background:var(--red)}
.feature{position:absolute;left:398px;width:126px;height:116px;background:var(--red);padding:4px}
.feature-inner{width:100%;height:100%;background:var(--white);padding:6px}
.photo{width:100%;height:100%}
.phone-block{position:absolute;font-family:"Oswald",sans-serif;font-weight:500;color:var(--white);display:flex;align-items:center}
/* gallery */
.tile{position:absolute;width:148px;height:148px;background:var(--red);padding:4px}
.tile-inner{width:100%;height:100%;background:var(--white);padding:6px}
.tile-inner .photo{background:#bdbdbd}
</style>
</head>
<body>
<div class="stage">

  <!-- FRONT: product lines -->
  <section class="page page-front">
    <svg class="header-shapes" width="529" height="94" viewBox="0 0 529 94" aria-hidden="true">
      <rect width="529" height="94" fill="#434345"/>
      <polygon points="0,0 200,0 178,70 0,70" fill="#fff"/>
      <polygon points="200,0 212,0 190,70 178,70" fill="#e31b23"/>
      <polygon points="0,70 186,70 178,94 0,94" fill="#e31b23"/>
    </svg>
    <div class="brand" style="left:14px;top:20px;font-size:20px"><span class="brand-mark"></span>Pellmont<br>Industries</div>
    <div class="url" style="left:14px;top:76px;font-size:10px">www.pellmontindustries.com</div>
    <h1 class="title" style="left:220px;top:14px;font-size:17.5px">Distribution, Contract Manufacturing<br>&amp; System Integration</h1>
    <div class="address" style="left:200px;top:76px">
      <svg width="9" height="12" viewBox="0 0 9 12" aria-hidden="true"><path d="M4.5 0A4.5 4.5 0 0 0 0 4.5C0 8 4.5 12 4.5 12S9 8 9 4.5A4.5 4.5 0 0 0 4.5 0Zm0 6.3a1.8 1.8 0 1 1 0-3.6 1.8 1.8 0 0 1 0 3.6Z" fill="#fff"/></svg>
      2210 HARLOW AVE. BROOKFIELD, IL 60513
    </div>

    <div class="line" style="top:110px">
      <div class="line-bar"><div class="line-accent"></div>
        <ul class="line-list list-main"><li>Power Distribution Modules</li><li>Circuit Breakers</li><li>Fuses</li></ul>
        <ul class="line-list list-accent"><li>Rocker &amp; Toggle Switches</li><li>CAN Switches</li><li>Battery Disconnects</li></ul>
      </div>
      <div class="badge octagon"><div class="badge-face octagon">NORVEL<br>Transport</div></div>
    </div>

    <div class="line" style="top:180px">
      <div class="line-bar"><div class="line-accent"></div>
        <ul class="line-list list-main"><li>Battery Equalizers</li><li>Power Converters</li><li>True Sine Wave Inverters</li></ul>
        <ul class="line-list list-accent"><li>Battery Separators</li><li>Interconnect Controllers</li><li>Battery Isolators</li></ul>
      </div>
      <div class="badge octagon"><div class="badge-face octagon">NORVEL<br>Power</div></div>
    </div>

    <div class="line" style="top:250px">
      <div class="line-bar"><div class="line-accent"></div>
        <ul class="line-list list-main"><li>Battery Disconnects</li><li>Battery Switches</li></ul>
        <ul class="line-list list-accent"><li>Mono-Stable Relays</li><li>Bi-Stable Relays</li></ul>
      </div>
      <div class="badge octagon"><div class="badge-face octagon">BRANTEX</div></div>
    </div>

    <div class="line" style="top:320px">
      <div class="line-bar" style="top:2px;height:54px">
        <ul class="line-list list-main" style="top:20px"><li>On Vehicle &amp; Mobile Equipment Displays</li></ul>
      </div>
      <div class="badge octagon"><div class="badge-face octagon">VANDORF</div></div>
    </div>

    <div class="line" style="top:390px">
      <div class="line-bar"><div class="line-accent"></div>
        <ul class="line-list list-main" style="top:9px"><li>HMIs Displays</li><li>SCADA Software</li></ul>
        <ul class="line-list list-accent" style="top:15px"><li>HMI + PLC Hybrids</li></ul>
      </div>
      <div class="badge octagon"><div class="badge-face octagon">KIROVA</div></div>
    </div>

    <div class="line" style="top:460px">
      <div class="line-bar"><div class="line-accent"></div>
        <ul class="line-list list-main"><li>Automation</li><li>Cables</li><li>Connectors</li></ul>
        <ul class="line-list list-accent"><li>Passive Distributors</li><li>DIN Valve Connectors</li><li>Industrial Ethernet/Connectors</li></ul>
      </div>
      <div class="badge octagon"><div class="badge-face octagon">Halden<br>Automation</div></div>
    </div>

    <div class="line" style="top:530px">
      <div class="line-bar"><div class="line-accent"></div>
        <ul class="line-list list-main"><li>Fuses</li><li>Fuse Blocks</li><li>Fuse Holders</li></ul>
        <ul class="line-list list-accent"><li>Circuit Breakers</li><li>Resettable Fuses</li><li>Fuse Accessories</li></ul>
      </div>
      <div class="badge octagon"><div class="badge-face octagon" style="color:#2a2a2b">FUSETRA</div></div>
    </div>

    <div class="line" style="top:600px">
      <div class="line-bar"><div class="line-accent"></div>
        <ul class="line-list list-main"><li>Custom Assemblies</li><li>Wire Harnesses</li><li>Testing</li></ul>
        <ul class="line-list list-accent"><li>Product Integration</li><li>Custom Bus</li><li>Bars Kitting</li></ul>
      </div>
      <div class="badge octagon"><div class="badge-face octagon" style="color:#2a2a2b">PELLMONT</div></div>
    </div>

    <div class="abs" style="left:504px;top:120px;width:25px;height:532px;background:var(--red)"></div>
    <div class="feature octagon" style="top:124px"><div class="feature-inner octagon"><div class="photo octagon" role="img" aria-label="Black power distribution case with fuses" style="background:linear-gradient(135deg,#d9d9d9,#3a3a3a)"></div></div></div>
    <div class="feature octagon" style="top:246px"><div class="feature-inner octagon"><div class="photo octagon" role="img" aria-label="Red battery disconnect switch" style="background:linear-gradient(160deg,#d8262c,#8a6d2f)"></div></div></div>
    <div class="feature octagon" style="top:368px"><div class="feature-inner octagon"><div class="photo octagon" role="img" aria-label="Fuse and relay distribution box" style="background:linear-gradient(135deg,#3c3c3c,#c8312f)"></div></div></div>

    <div class="abs" role="img" aria-label="Technician in a red hard hat and work jacket" style="left:388px;top:498px;width:141px;height:154px;background:linear-gradient(180deg,#e4e4e4 0%,#8d8d90 60%,#2d2d30 100%)"></div>
    <div class="phone-block" style="left:378px;top:652px;width:151px;height:37px;background:var(--black);justify-content:center;font-size:19px">555 210 4830</div>
  </section>

  <!-- BACK: capabilities -->
  <section class="page page-back">
    <svg class="header-shapes" width="530" height="128" viewBox="0 0 530 128" aria-hidden="true">
      <rect width="530" height="128" fill="#434345"/>
      <polygon points="0,0 270,0 245,94 0,94" fill="#fff"/>
      <polygon points="270,0 282,0 257,94 245,94" fill="#e31b23"/>
      <polygon points="0,94 253,94 244,128 0,128" fill="#e31b23"/>
      <rect x="282" y="94" width="248" height="4" fill="#e31b23"/>
    </svg>
    <div class="brand" style="left:22px;top:26px;font-size:25px"><span class="brand-mark" style="width:15px;height:15px"></span>Pellmont<br>Industries</div>
    <div class="url" style="left:18px;top:103px;font-size:12.5px">www.pellmontindustries.com</div>
    <h2 class="title" style="left:282px;top:20px;font-size:24px;line-height:1.05">Distribution,<br>Contract Manufacturing<br>&amp; System Integration</h2>

    <div class="tile octagon" style="left:30px;top:152px"><div class="tile-inner octagon"><div class="photo octagon" role="img" aria-label="Red battery switches mounted on a panel" style="background:linear-gradient(135deg,#c0282d,#777)"></div></div></div>
    <div class="tile octagon" style="left:189px;top:152px"><div class="tile-inner octagon"><div class="photo octagon" role="img" aria-label="Control module with colored wiring" style="background:linear-gradient(135deg,#8a8a8a,#4a5a6a)"></div></div></div>
    <div class="tile octagon" style="left:348px;top:152px"><div class="tile-inner octagon"><div class="photo octagon" role="img" aria-label="Terminal block panel with yellow fuses" style="background:linear-gradient(135deg,#d8d2c0,#9b8f63)"></div></div></div>
    <div class="tile octagon" style="left:30px;top:314px"><div class="tile-inner octagon"><div class="photo octagon" role="img" aria-label="Row of red switches on an assembly board" style="background:linear-gradient(135deg,#d9d3c5,#b94040)"></div></div></div>
    <div class="tile octagon" style="left:189px;top:314px"><div class="tile-inner octagon"><div class="photo octagon" role="img" aria-label="Wire harness laid out on a build board" style="background:linear-gradient(135deg,#d8c7a8,#8d7b62)"></div></div></div>
    <div class="tile octagon" style="left:348px;top:314px"><div class="tile-inner octagon"><div class="photo octagon" role="img" aria-label="Black enclosure with cable assembly" style="background:linear-gradient(135deg,#cfcfcf,#2b2b2b)"></div></div></div>
    <div class="tile octagon" style="left:30px;top:474px"><div class="tile-inner octagon"><div class="photo octagon" role="img" aria-label="Electrical control panel with relays" style="background:linear-gradient(135deg,#e0e0e0,#6d6d70)"></div></div></div>
    <div class="tile octagon" style="left:189px;top:474px"><div class="tile-inner octagon"><div class="photo octagon" role="img" aria-label="Distribution panel with yellow connectors" style="background:linear-gradient(135deg,#d4d0c4,#8a8440)"></div></div></div>
    <div class="tile octagon" style="left:348px;top:474px"><div class="tile-inner octagon"><div class="photo octagon" role="img" aria-label="Cabinet with bundled red wiring" style="background:linear-gradient(135deg,#3a3a3a,#c23838)"></div></div></div>

    <svg class="abs" style="left:0;top:652px" width="530" height="37" viewBox="0 0 530 37" aria-hidden="true">
      <rect width="530" height="37" fill="#434345"/>
      <polygon points="352,0 530,0 530,37 340,37" fill="#e31b23"/>
    </svg>
    <div class="address" style="left:26px;top:656px;font-size:10.5px">
      <svg width="9" height="12" viewBox="0 0 9 12" aria-hidden="true"><path d="M4.5 0A4.5 4.5 0 0 0 0 4.5C0 8 4.5 12 4.5 12S9 8 9 4.5A4.5 4.5 0 0 0 4.5 0Zm0 6.3a1.8 1.8 0 1 1 0-3.6 1.8 1.8 0 0 1 0 3.6Z" fill="#fff"/></svg>
      2210 HARLOW AVE. BROOKFIELD, IL 60513
    </div>
    <div class="address" style="left:26px;top:671px;font-size:10.5px">
      <svg width="10" height="10" viewBox="0 0 10 10" aria-hidden="true"><rect x="2" y="0" width="6" height="3" fill="#fff"/><rect x="0" y="3" width="10" height="5" rx="1" fill="#fff"/><rect x="2" y="6" width="6" height="4" fill="#fff"/></svg>
      FAX: (555) 210-4836
    </div>
    <div class="phone-block" style="left:364px;top:652px;height:37px;gap:8px;font-size:22px">
      <svg width="22" height="22" viewBox="0 0 22 22" aria-hidden="true"><circle cx="11" cy="11" r="10" fill="none" stroke="#fff" stroke-width="1.6"/><path d="M7.5 6c.5-.4 1.2-.3 1.5.2l1 1.7c.3.5.2 1-.2 1.4l-.6.5c.5 1.2 1.5 2.2 2.7 2.8l.5-.6c.4-.4 1-.5 1.4-.2l1.7 1c.5.3.6 1 .2 1.5l-.7.8c-.6.6-1.5.8-2.3.4-2.6-1.2-4.6-3.2-5.8-5.8-.4-.8-.2-1.7.4-2.3Z" fill="#fff"/></svg>
      555 210 4830
    </div>
  </section>

</div>
</body>
</html>
```